Building business client journey document

We want to design a journey document which helps our clients understand the process of building a house from initial conversations through to construction. I have attached an example along with the design of stages/writing we would like for ours.

```html
<!DOCTYPE html>
<html lang="en">
<head>
<meta charset="utf-8">
<title>Journey to Your New Home</title>
<link href="https://fonts.googleapis.com/css2?family=Oswald:wght@400;500;600&family=Source+Sans+3:wght@400;600&display=swap" rel="stylesheet">
<style>
  :root {
    --green-dark: #1b6b3a;
    --green: #1f7d45;
    --green-bright: #27a65c;
    --charcoal: #333333;
    --ink: #222222;
    --paper: #f3f3f3;
    --sky: #b7e0ea;
    --sun: #e8b04a;
    --white: #ffffff;
  }
  html, body { margin: 0; padding: 0; overflow: hidden; background: var(--white); }
  .journey {
    position: relative;
    width: 673px;
    height: 1200px;
    overflow: hidden;
    background: linear-gradient(180deg, var(--paper) 0%, #fafafa 50%, var(--paper) 100%);
    font-family: "Source Sans 3", Arial, sans-serif;
    color: var(--ink);
  }
  .journey-header {
    position: absolute; left: 0; top: 0; width: 673px; height: 62px;
    background: var(--green-dark);
    display: flex; align-items: center; justify-content: center;
  }
  .journey-title {
    margin: 0; font-family: "Oswald", sans-serif; font-weight: 600;
    font-size: 30px; color: var(--white); letter-spacing: 0.3px;
  }
  .stage-bar {
    position: absolute; height: 24px; background: var(--charcoal);
    clip-path: polygon(0 0, calc(100% - 14px) 0, 100% 50%, calc(100% - 14px) 100%, 0 100%);
    font-family: "Oswald", sans-serif; font-weight: 500; color: var(--white); font-size: 13.5px;
  }
  .stage-bar .stage-number { position: absolute; left: 14px; top: 3px; }
  .stage-bar .stage-phase { position: absolute; left: 0; right: 0; top: 3px; text-align: center; }

  .step-icon {
    position: absolute; width: 58px; height: 58px; border-radius: 8px;
    background: linear-gradient(135deg, #4a4a4a, #2a2a2a); opacity: 0.85;
  }
  .step-card {
    position: absolute; width: 168px; box-sizing: border-box;
    border: 3px solid var(--green-bright); border-radius: 9px;
    background: var(--white); padding: 8px 9px 8px 12px;
    overflow: hidden;
  }
  .step-card h3 {
    margin: 2px 0 5px; text-align: center; font-family: "Oswald", sans-serif;
    font-weight: 500; font-size: 11.5px; color: var(--green-bright); line-height: 1.3;
  }
  .step-card p { margin: 0; font-size: 10.4px; line-height: 1.3; }
  .step-card ol { margin: 8px 0 0; padding: 0; list-style: none; font-size: 10.4px; line-height: 1.3; }
  .cost-badge {
    position: absolute; width: 22px; height: 22px; border-radius: 50%;
    background: var(--green-bright); border: 2px solid var(--white);
    color: var(--white); font-family: "Oswald", sans-serif; font-weight: 600;
    font-size: 14px; line-height: 22px; text-align: center;
  }
  .flow-arrow {
    position: absolute; width: 38px; height: 20px; background: var(--charcoal);
    clip-path: polygon(0 0, 78% 0, 100% 50%, 78% 100%, 0 100%, 10% 50%);
  }
  .variation-note {
    position: absolute; left: 386px; top: 650px; width: 112px;
    text-align: center; font-size: 10.4px; line-height: 1.3;
  }
  .variation-post {
    position: absolute; left: 584px; top: 620px; width: 20px; height: 80px;
    background: var(--charcoal);
  }
  .variation-line {
    position: absolute; left: 438px; top: 704px; width: 10px; height: 176px;
    background: repeating-linear-gradient(135deg, var(--charcoal) 0 1.5px, transparent 1.5px 4px);
  }
  .construction-path { position: absolute; left: 0; top: 940px; }
  .construction-path text {
    font-family: "Oswald", sans-serif; font-weight: 500; font-size: 12.5px; fill: var(--white);
  }
  .journey-footer {
    position: absolute; left: 0; top: 1128px; width: 673px; height: 72px;
    background: var(--charcoal); color: var(--white);
  }
  .footer-name {
    position: absolute; left: 34px; top: 25px; font-family: "Oswald", sans-serif;
    font-weight: 600; font-size: 16px; color: var(--green-bright);
  }
  .footer-contact {
    position: absolute; right: 28px; top: 7px; text-align: right;
    font-size: 11px; line-height: 1.3;
  }
  .footer-contact strong { font-family: "Oswald", sans-serif; font-weight: 600; font-size: 11.5px; }
</style>
</head>
<body>
<main class="journey">
  <header class="journey-header"><h1 class="journey-title">JOURNEY TO YOUR NEW HOME</h1></header>

  <div class="stage-bar" style="left:14px; top:80px; width:644px;">
    <span class="stage-number">STAGE 1:</span><span class="stage-phase">INITIAL PHASE</span>
  </div>

  <div class="step-icon" role="img" aria-label="Icon of a hand holding a phone" style="left:95px; top:118px;"></div>
  <div class="step-icon" role="img" aria-label="Icon of two people shaking hands" style="left:308px; top:118px;"></div>
  <div class="step-icon" role="img" aria-label="Icon of a document, pencil and calculator" style="left:521px; top:118px;"></div>

  <section class="step-card" style="left:40px; top:186px; height:132px;">
    <h3>INITIAL CONTACT</h3>
    <p>This is usually by phone or email quick chat with builder - Mel Harlow then an email will be sent with questioniare for you to fill out to see if were a match to work together.</p>
  </section>
  <section class="step-card" style="left:253px; top:186px; height:132px;">
    <h3>INITIAL FACE TO FACE</h3>
    <p>This is were we ciscuss more in depth about your prospect and talk about how we can help you.</p>
  </section>
  <section class="step-card" style="left:466px; top:186px; height:132px;">
    <h3>1ST BAG PACK ESTIMATE</h3>
    <p>At this stage we will provide you with your 1st initial estimate based on you previous discussions so we can deliver you the best possible product for your budget ( 2-3 days).</p>
  </section>

  <div class="stage-bar" style="left:14px; top:342px; width:644px;">
    <span class="stage-number">STAGE 2:</span><span class="stage-phase">PRELIMINARY PHASE</span>
  </div>

  <div class="step-icon" role="img" aria-label="Icon of a handshake" style="left:95px; top:380px;"></div>
  <div class="step-icon" role="img" aria-label="Icon of a house" style="left:308px; top:380px;"></div>
  <div class="step-icon" role="img" aria-label="Icon of a calculator inside refresh arrows" style="left:521px; top:380px;"></div>

  <section class="step-card" style="left:40px; top:450px; height:165px;">
    <h3>1ST PRELIMINARY AGREEMENT</h3>
    <p>To move forward from forward both parties needs to sign a preliminary agreement to we can organize the following:</p>
    <ol><li>1. Soil test</li><li>2. Contour survey</li><li>3. BAL report ( if requires)</li><li>(10 days)</li></ol>
  </section>
  <div class="cost-badge" style="left:195px; top:439px;">$</div>
  <div class="flow-arrow" style="left:212px; top:517px;"></div>

  <section class="step-card" style="left:253px; top:450px; height:165px;">
    <h3>CONCEPT DRAWINGS</h3>
    <p>This is were your plans come together on paper and you get a good feel of what your projectwill look like. This is the 2nd Prelim Agreement. (5 days)</p>
  </section>
  <div class="cost-badge" style="left:408px; top:439px;">$</div>
  <div class="flow-arrow" style="left:425px; top:517px;"></div>

  <section class="step-card" style="left:466px; top:450px; height:165px;">
    <h3>UPDATE ESTIMATE</h3>
    <p>This is where we can make any updates to your previous estimate, also submit planning approval if required. (2 days)</p>
  </section>

  <div class="step-icon" role="img" aria-label="Icon of a contract being signed" style="left:95px; top:636px;"></div>
  <div class="step-icon" role="img" aria-label="Icon of a paint tin" style="left:308px; top:636px;"></div>
  <div class="variation-note">Any changes past this point is a variation to the quote.</div>
  <div class="step-icon" role="img" aria-label="Icon of a rolled house plan" style="left:512px; top:630px;"></div>
  <div class="variation-post"></div>
  <div class="variation-line"></div>

  <section class="step-card" style="left:40px; top:708px; height:172px;">
    <h3>SIGN CONTRACT</h3>
    <p>Sign contract, pay deposit from here. We prepare your plans for building permit.</p>
  </section>
  <div class="cost-badge" style="left:195px; top:697px;">$</div>
  <div class="flow-arrow" style="left:212px; top:778px;"></div>

  <section class="step-card" style="left:253px; top:708px; height:172px;">
    <h3>COLOUR SELECTION</h3>
    <p>From here we will provide you with a interior designer to help you with your decsions and have a list of competitive suppliers to chose your list from.</p>
  </section>
  <div class="flow-arrow" style="left:425px; top:778px;"></div>

  <section class="step-card" style="left:466px; top:708px; height:172px; padding-top:5px;">
    <h3 style="margin-bottom:4px;">CONSTRUCTION DRAWINGS<br>&amp; ENGINEERING</h3>
    <p style="line-height:1.26;">Here we finance construction drawings which coincide with the engineer drawings make any amendments to the estimate. This is the 3rd agreement, from here we can also prepare your, CAC and energy assessment ready for building permit (10-15 days)</p>
  </section>
  <div class="cost-badge" style="left:621px; top:697px;">$</div>

  <div class="stage-bar" style="left:20px; top:902px; width:642px;">
    <span class="stage-number">STAGE 3:</span><span class="stage-phase">CONSTRUCTION STAGE</span>
  </div>

  <svg class="construction-path" width="673" height="180" viewBox="0 940 673 180" aria-label="Construction stage steps">
    <rect x="0" y="1034" width="210" height="74" fill="var(--sky)"/>
    <rect x="28" y="1036" width="96" height="70" rx="6" fill="var(--sun)" opacity="0.85" role="img" aria-label="Illustration of a finished family home"/>
    <path d="M536 985 H564 A43 43 0 0 1 564 1071 H520" fill="none" stroke="var(--green)" stroke-width="74"/>
    <g stroke="var(--white)" stroke-width="3">
      <polygon points="52,948 172,948 186,985 172,1022 52,1022 66,985" fill="var(--green)"/>
      <polygon points="172,948 296,948 310,985 296,1022 172,1022 186,985" fill="var(--green-dark)"/>
      <polygon points="296,948 420,948 434,985 420,1022 296,1022 310,985" fill="var(--green)"/>
      <polygon points="420,948 544,948 558,985 544,1022 420,1022 434,985" fill="var(--green-dark)"/>
      <polygon points="142,1034 256,1034 242,1071 256,1108 142,1108 128,1071" fill="var(--green)"/>
      <polygon points="256,1034 380,1034 366,1071 380,1108 256,1108 242,1071" fill="var(--green-dark)"/>
      <polygon points="380,1034 504,1034 490,1071 504,1108 380,1108 366,1071" fill="var(--green)"/>
      <polygon points="504,1034 566,1034 566,1108 504,1108 490,1071" fill="var(--green-dark)" stroke="none"/>
    </g>
    <text x="114" y="982" text-anchor="middle">BUILDING PERMIT</text>
    <text x="114" y="999" text-anchor="middle">APPLICATION</text>
    <text x="238" y="982" text-anchor="middle">PROJECT</text>
    <text x="238" y="999" text-anchor="middle">SCHEDULING</text>
    <text x="360" y="990" text-anchor="middle">SLAB DOWN</text>
    <text x="483" y="990" text-anchor="middle">WALL PLATE</text>
    <text x="196" y="1076" text-anchor="middle">HAND OVER</text>
    <text x="318" y="1076" text-anchor="middle">RIT OUT</text>
    <text x="441" y="1076" text-anchor="middle">LOCK UP</text>
    <text x="565" y="1076" text-anchor="middle">ROOF ON</text>
  </svg>

  <footer class="journey-footer">
    <div class="footer-name">NORTHVALE HOMES</div>
    <div class="footer-contact">
      <strong>NORTHVALE HOMES</strong><br>
      14 Harbour Lane, Seaford, WA, 6199<br>
      hello@northvalehomes.com.au<br>
      www.northvalehomes.com.au
    </div>
  </footer>
</main>
</body>
</html>
```